modernized upgrade to existing squarespace site

Hello! I have the following page for my consulting firm: https://hollinbrookcounsel.com/ Would love to upgrade to something more modern/attractive like here: https://www.pemberlowgroup.com/ or https://brightquillstudio.com/ , but I am open to creativity. Would like to retain the logo look and color theme from the logo. The rest can be left to creative discretion.

```html
<!DOCTYPE html>
<html lang="en">
<head>
<meta charset="utf-8">
<title>Hollinbrook Counsel</title>
<link href="https://fonts.googleapis.com/css2?family=Marcellus&family=Poppins:wght@300;400;500;600&display=swap" rel="stylesheet">
<style>
:root{
  --navy:#1b2a40;
  --rose:#c4918a;
  --rose-light:#d9aba4;
  --ink:#1d1d1f;
  --dark:#141414;
  --grey:#6b6b6b;
  --line:#9a9a9a;
  --white:#ffffff;
  --serif:'Marcellus', serif;
  --sans:'Poppins', sans-serif;
}
*{margin:0;padding:0;box-sizing:border-box}
html,body{width:1200px;height:3659px;overflow:hidden;background:var(--white)}
body{position:relative;font-family:var(--sans);color:var(--ink)}
.abs{position:absolute}
.serif{font-family:var(--serif);font-weight:400}

/* nav */
.topbar{left:0;top:0;width:1200px;height:52px;background:var(--navy)}
.brand{display:flex;align-items:center;gap:10px;color:var(--white)}
.brand-box{width:36px;height:36px;border:1.5px solid var(--white)}
.brand-name{font-family:var(--serif);font-size:20px;letter-spacing:3px;line-height:1}
.brand-sub{font-family:var(--serif);font-size:9px;letter-spacing:2px;color:var(--rose-light)}
.nav-link{top:18px;font-size:12px;color:var(--white)}
.nav-link.active{color:var(--rose-light)}
.nav-icon{top:15px;width:22px;height:22px;border:1.5px solid var(--white);border-radius:50%}
.nav-cta{left:968px;top:11px;width:110px;height:30px;border:1.5px solid var(--white);color:var(--white);font-size:11px;font-weight:500;display:flex;align-items:center;justify-content:center}

/* hero */
.hero-photo{left:0;top:52px;width:1200px;height:535px;background:linear-gradient(180deg,#1d3656 0%,#4b5c70 35%,#b78a5a 62%,#6a4a32 82%,#2f241d 100%)}
.hero-title{left:105px;top:250px;font-size:104px;color:var(--white);letter-spacing:2px;line-height:1}
.hero-sub{left:118px;top:362px;font-size:37px;color:var(--white);line-height:45px}
.play{border-radius:50%;background:var(--white);display:flex;align-items:center;justify-content:center;box-shadow:0 0 0 6px rgba(255,255,255,.35)}
.hero-frame{left:873px;top:108px;width:240px;height:479px;border:3px solid var(--white);border-bottom:none}

/* section titles */
.section-title{width:1200px;left:0;text-align:center;font-size:36px;color:var(--ink)}

/* services */
.service-card{top:679px;width:306px;height:362px;border:1.5px solid #8a8a8a;background:var(--white)}
.service-icon{left:7px;top:7px;width:68px;height:58px;background:var(--rose)}
.service-name{left:6px;top:76px;font-size:18px;color:var(--ink)}
.service-photo{left:7px;top:116px;width:290px;height:238px}
.btn-dark{background:var(--ink);color:var(--white);font-size:10.5px;font-weight:600;display:flex;align-items:center;justify-content:center;letter-spacing:.3px}

/* about */
.about-band{left:122px;top:1146px;width:956px;height:588px;background:var(--rose)}
.about-title{left:133px;top:1194px;font-size:38px;color:var(--white)}
.about-rule{left:297px;top:1218px;width:64px;height:1.5px;background:var(--white)}
.about-text{left:133px;top:1242px;width:470px;font-size:11px;line-height:15px;color:var(--white)}
.about-frame{left:502px;top:1322px;width:408px;height:385px;border:1.5px solid #3a2b29}
.about-photo{left:133px;top:1330px;width:765px;height:392px;background:linear-gradient(180deg,#151c1c 0%,#2b3535 55%,#1a2222 100%)}
.about-vertical{left:968px;top:1146px;width:588px;height:110px;transform-origin:0 0;transform:translate(110px,0) rotate(90deg);font-size:90px;color:var(--white);line-height:110px;text-align:center;overflow:hidden;white-space:nowrap}

/* partners */
.partner{top:1842px;width:182px;height:110px;background:var(--white);box-shadow:0 2px 10px rgba(0,0,0,.09);display:flex;align-items:center;justify-content:center}
.partner-badge{width:90px;height:48px;background:#b9b9b9}
.slider-dot{top:1887px;width:20px;height:20px;border-radius:50%;background:#8d8d8d;display:flex;align-items:center;justify-content:center}

/* testimonials */
.testimonial-band{left:0;top:2013px;width:1200px;height:479px;background:linear-gradient(120deg,#3d3d3d 0%,#5c5c5c 45%,#4a4a4a 70%,#2f2f2f 100%)}
.testimonial-title{left:120px;top:2068px;font-size:38px;color:var(--white)}
.avatar{left:123px;top:2126px;width:50px;height:50px;border-radius:50%;background:#8c8c8c}
.client-name{left:194px;top:2134px;font-size:15px;font-weight:500;color:var(--white)}
.client-date{font-size:10px;font-weight:400;margin-left:6px}
.stars{left:194px;top:2156px;display:flex;gap:3px}
.quote-text{left:122px;top:2227px;width:350px;font-size:11px;line-height:18px;color:#ececec}
.arrow-pair{left:124px;top:2315px;width:130px;height:35px;background:var(--rose);display:flex}
.arrow-pair span{flex:1;display:flex;align-items:center;justify-content:center}
.arrow-pair span+span{border-left:1.5px solid var(--rose-light)}
.ghost-word{left:0;top:2370px;font-size:150px;color:rgba(255,255,255,.12);line-height:1;white-space:nowrap}
.portrait-frame{left:700px;top:2115px;width:378px;height:377px;border:8px solid var(--white);border-bottom:none}
.portrait{left:712px;top:2127px;width:354px;height:353px;background:linear-gradient(180deg,#9c9c9c 0%,#6f6f6f 60%,#3e3e3e 100%)}

/* news */
.feature-photo{left:133px;top:2552px;width:487px;height:278px;background:linear-gradient(135deg,#103245 0%,#3f7d96 45%,#a9d4e0 65%,#2e5f78 100%)}
.feature-strip{left:624px;top:2552px;width:32px;height:278px;background:var(--rose)}
.feature-strip-text{left:624px;top:2552px;width:278px;height:32px;transform-origin:0 0;transform:translate(0,278px) rotate(-90deg);font-family:var(--serif);font-size:16px;color:var(--white);letter-spacing:1px;text-align:center;line-height:32px;white-space:nowrap}
.news-date{font-family:var(--serif);font-size:10.5px;color:var(--rose);display:flex;align-items:center;gap:7px}
.news-headline{font-size:15px;line-height:22px;color:var(--ink)}
.news-thumb{left:744px;width:127px;height:91px}
.news-small{left:885px;width:200px;font-size:13.5px;line-height:17px}
.news-rule{left:744px;width:314px;height:1px;background:#cfcfcf}

/* contact */
.map{left:0;top:2978px;width:654px;height:443px;background:linear-gradient(160deg,#e6efe2 0%,#dde8ee 55%,#c8dcea 100%)}
.map-card{left:200px;top:3186px;width:220px;height:62px;background:var(--white);font-size:12.5px;text-align:center;line-height:18px;display:flex;align-items:center;justify-content:center;box-shadow:0 2px 8px rgba(0,0,0,.15)}
.contact-panel{left:654px;top:2978px;width:546px;height:443px;background:var(--rose)}
.contact-title{left:722px;top:3030px;font-size:34px;line-height:38px;color:var(--white)}
.contact-sub{left:723px;top:3108px;font-size:12px;color:var(--white)}
.field{left:723px;width:354px;border:1px solid var(--white);color:var(--white);font-size:11px;padding:9px 11px}

/* footer */
.footer{left:0;top:3421px;width:1200px;height:238px;background:var(--dark)}
.footer-rule{top:3450px;width:1px;height:170px;background:#555}
.footer-head{top:3452px;font-family:var(--serif);font-size:18px;color:var(--white)}
.footer-links{left:477px;top:3484px;font-size:9.5px;color:var(--white);line-height:20.8px;list-style:none}
.footer-item{font-size:9.5px;color:var(--white);display:flex;align-items:flex-start;gap:8px;line-height:13px}
.icon-ring{width:17px;height:17px;border:1px solid var(--white);border-radius:50%;flex:none}
.copyright{left:0;top:3634px;width:1200px;text-align:center;font-size:8.5px;color:var(--white)}
.copyright-rule{left:120px;top:3625px;width:958px;height:1px;background:#444}
</style>
</head>
<body>

<!-- Navigation -->
<header class="abs topbar"></header>
<div class="abs brand" style="left:120px;top:7px">
  <div class="brand-box"></div>
  <div><div class="brand-name">HOLLINBROOK</div><div class="brand-sub">COUNSEL</div></div>
</div>
<span class="abs nav-link active" style="left:435px">Home</span>
<span class="abs nav-link" style="left:511px">Services</span>
<span class="abs nav-link" style="left:600px">Research</span>
<span class="abs nav-link" style="left:697px">The Institute</span>
<span class="abs nav-link" style="left:810px">In the News</span>
<div class="abs nav-icon" style="left:898px">
  <svg width="19" height="19" viewBox="0 0 19 19"><circle cx="8.5" cy="8.5" r="3.5" fill="none" stroke="#fff" stroke-width="1.4"/><path d="M11 11l3 3" stroke="#fff" stroke-width="1.4"/></svg>
</div>
<div class="abs nav-icon" style="left:930px">
  <svg width="19" height="19" viewBox="0 0 19 19"><circle cx="9.5" cy="7" r="3" fill="#fff"/><path d="M4 16c1-4 10-4 11 0" fill="#fff"/></svg>
</div>
<div class="abs nav-cta">CONTACT US</div>

<!-- Hero -->
<div class="abs hero-photo" role="img" aria-label="City skyline at sunset with an observation tower and distant mountains"></div>
<h1 class="abs serif hero-title">HOLLINBROOK</h1>
<p class="abs serif hero-sub">Macroeconomic &amp; policy Analytics<br>for today’s turbulent environment.</p>
<div class="abs play" style="left:131px;top:474px;width:52px;height:52px">
  <svg width="30" height="30" viewBox="0 0 30 30"><circle cx="15" cy="15" r="14" fill="#1d1d1f"/><path d="M12 9l9 6-9 6z" fill="#fff"/></svg>
</div>
<div class="abs hero-frame"></div>

<!-- Services -->
<h2 class="abs serif section-title" style="top:618px">Our Services</h2>

<article class="abs service-card" style="left:122px">
  <div class="abs service-icon"><svg width="68" height="58" viewBox="0 0 68 58"><circle cx="32" cy="27" r="12" fill="none" stroke="#fff" stroke-width="2"/><path d="M41 36l9 9" stroke="#fff" stroke-width="2.5"/><path d="M25 30l5-5 4 3 5-6" fill="none" stroke="#fff" stroke-width="1.6"/></svg></div>
  <div class="abs service-name">Analytics &amp; Messaging &nbsp;→</div>
  <div class="abs service-photo" role="img" aria-label="Laptop showing an analytics dashboard" style="background:linear-gradient(160deg,#6b5a4c 0%,#2e3338 45%,#a7b3ba 70%,#4a4d52 100%)"></div>
</article>
<article class="abs service-card" style="left:446px">
  <div class="abs service-icon"><svg width="68" height="58" viewBox="0 0 68 58"><rect x="24" y="14" width="20" height="28" fill="none" stroke="#fff" stroke-width="2"/><circle cx="34" cy="25" r="4" fill="none" stroke="#fff" stroke-width="1.6"/><path d="M28 35h12M28 38h12" stroke="#fff" stroke-width="1.4"/></svg></div>
  <div class="abs service-name">Customized Reports &nbsp;→</div>
  <div class="abs service-photo" role="img" aria-label="Hands leafing through a printed report" style="background:linear-gradient(150deg,#2a2c30 0%,#4d4f53 45%,#c9c5bd 75%,#6c6a66 100%)"></div>
</article>
<article class="abs service-card" style="left:770px">
  <div class="abs service-icon"><svg width="68" height="58" viewBox="0 0 68 58"><rect x="23" y="14" width="20" height="28" fill="none" stroke="#fff" stroke-width="2"/><path d="M27 21l2 2 3-3M27 29l2 2 3-3M35 22h5M35 30h5M27 37h13" fill="none" stroke="#fff" stroke-width="1.4"/><path d="M45 20l4 4-8 9-3 1 1-3z" fill="none" stroke="#fff" stroke-width="1.4"/></svg></div>
  <div class="abs service-name">Proprietary Surveys &nbsp;→</div>
  <div class="abs service-photo" role="img" aria-label="People reviewing charts on a laptop and tablet" style="background:linear-gradient(150deg,#c9b48a 0%,#e9e2cf 40%,#8f9ea4 70%,#b9a988 100%)"></div>
</article>

<div class="abs btn-dark" style="left:527px;top:1060px;width:145px;height:36px">VIEW ALL SERVICES</div>

<!-- About -->
<section class="abs about-band"></section>
<h2 class="abs serif about-title">About Us</h2>
<div class="abs about-rule"></div>
<p class="abs about-text">Our services suite focuses on providing exclusive, custom research and analytics to a select number of clients. We do so by outlining a sophisticated research plan, building teams of industry experts, and providing final analyses catered to your preferred audience.</p>
<div class="abs btn-dark" style="left:782px;top:1238px;width:116px;height:34px">READ MORE</div>
<div class="abs about-frame"></div>
<div class="abs about-photo" role="img" aria-label="Night view of a domed cathedral and river bridge"></div>
<div class="abs play" style="left:497px;top:1506px;width:42px;height:42px">
  <svg width="26" height="26" viewBox="0 0 26 26"><circle cx="13" cy="13" r="12" fill="#1d1d1f"/><path d="M10 8l8 5-8 5z" fill="#fff"/></svg>
</div>
<div class="abs serif about-vertical">HOLLINBROOK</div>

<!-- Partners -->
<h2 class="abs serif section-title" style="top:1780px">Our Partners</h2>
<div class="abs slider-dot" style="left:87px"><svg width="10" height="10" viewBox="0 0 10 10"><path d="M6 2L3 5l3 3" fill="none" stroke="#fff" stroke-width="1.5"/></svg></div>
<div class="abs partner" style="left:122px"><div class="partner-badge"></div></div>
<div class="abs partner" style="left:316px"><div class="partner-badge" style="width:100px;height:80px"></div></div>
<div class="abs partner" style="left:510px"><div class="partner-badge" style="width:104px;height:30px"></div></div>
<div class="abs partner" style="left:703px"><div class="partner-badge" style="width:114px;height:44px"></div></div>
<div class="abs partner" style="left:896px"><div class="partner-badge" style="width:120px;height:40px"></div></div>
<div class="abs slider-dot" style="left:1093px"><svg width="10" height="10" viewBox="0 0 10 10"><path d="M4 2l3 3-3 3" fill="none" stroke="#fff" stroke-width="1.5"/></svg></div>

<!-- Testimonials -->
<section class="abs testimonial-band" role="img" aria-label="Monochrome city skyline with tall towers"></section>
<div class="abs serif ghost-word">HOLLINBROOK</div>
<h2 class="abs serif testimonial-title">What Our Clients Say</h2>
<div class="abs avatar" role="img" aria-label="Client portrait"></div>
<div class="abs client-name">Arlen Voss<span class="client-date">21 April 2024</span></div>
<div class="abs stars">
  <svg width="80" height="13" viewBox="0 0 80 13">
    <g fill="#f1c21b">
      <path d="M6.5 0l2 4.3 4.5.5-3.4 3 1 4.5-4.1-2.4-4.1 2.4 1-4.5L0 4.8l4.5-.5z"/>
      <path transform="translate(16 0)" d="M6.5 0l2 4.3 4.5.5-3.4 3 1 4.5-4.1-2.4-4.1 2.4 1-4.5L0 4.8l4.5-.5z"/>
      <path transform="translate(32 0)" d="M6.5 0l2 4.3 4.5.5-3.4 3 1 4.5-4.1-2.4-4.1 2.4 1-4.5L0 4.8l4.5-.5z"/>
      <path transform="translate(48 0)" d="M6.5 0l2 4.3 4.5.5-3.4 3 1 4.5-4.1-2.4-4.1 2.4 1-4.5L0 4.8l4.5-.5z"/>
      <path transform="translate(64 0)" d="M6.5 0l2 4.3 4.5.5-3.4 3 1 4.5-4.1-2.4-4.1 2.4 1-4.5L0 4.8l4.5-.5z"/>
    </g>
  </svg>
</div>
<svg class="abs" style="left:122px;top:2196px" width="32" height="24" viewBox="0 0 32 24"><path d="M0 10q0-10 12-10v5q-6 0-6 5h6v14H0zM18 10q0-10 12-10v5q-6 0-6 5h6v14H18z" fill="#8f8f8f"/></svg>
<p class="abs quote-text">Lorem Ipsum is simply dummy text of the printing and typesetting industry. Lorem Ipsum has been the industry’s standard dummy text ever since the 1500s, when an unknown printer took a galley of type and scrambled it to make a type specimen book.</p>
<div class="abs arrow-pair">
  <span><svg width="24" height="10" viewBox="0 0 24 10"><path d="M23 5H2M6 1L2 5l4 4" fill="none" stroke="#fff" stroke-width="1.3"/></svg></span>
  <span><svg width="24" height="10" viewBox="0 0 24 10"><path d="M1 5h21M18 1l4 4-4 4" fill="none" stroke="#fff" stroke-width="1.3"/></svg></span>
</div>
<div class="abs portrait-frame"></div>
<div class="abs portrait" role="img" aria-label="Portrait of a client in a suit with arms crossed"></div>

<!-- News -->
<div class="abs feature-photo" role="img" aria-label="Digital medical technology interface over a researcher"></div>
<div class="abs feature-strip"></div>
<div class="abs feature-strip-text">HOLLINBROOK COUNSEL</div>
<div class="abs news-date" style="left:133px;top:2847px">
  <svg width="16" height="14" viewBox="0 0 16 14"><rect x=".5" y="1.5" width="15" height="12" fill="none" stroke="#c4918a"/><path d="M.5 4.5h15M4 0v3M12 0v3" stroke="#c4918a"/></svg>February 28, 2024
</div>
<p class="abs news-headline" style="left:133px;top:2869px;width:500px">“Medical Technology Industry Continues to Create High-Paying<br>&nbsp;Jobs at Small Businesses Throughout Pandemic.”</p>
<svg class="abs" style="left:139px;top:2920px" width="18" height="8" viewBox="0 0 18 8"><path d="M0 4h16M13 1l3 3-3 3" fill="none" stroke="#c4918a"/></svg>

<h2 class="abs serif" style="left:743px;top:2540px;font-size:36px">Latest News</h2>

<div class="abs news-thumb" role="img" aria-label="Spilled pill capsules" style="top:2610px;background:linear-gradient(135deg,#3a2a2a 0%,#c98a3a 45%,#e8e3dc 70%,#5a3d58 100%)"></div>
<div class="abs news-date" style="left:885px;top:2611px"><svg width="16" height="14" viewBox="0 0 16 14"><rect x=".5" y="1.5" width="15" height="12" fill="none" stroke="#c4918a"/><path d="M.5 4.5h15M4 0v3M12 0v3" stroke="#c4918a"/></svg>February 28, 2024</div>
<p class="abs news-small" style="top:2634px">Dr. Torvane: Medcover’s drug price ‘negotiations’ are anything but</p>
<svg class="abs" style="left:886px;top:2696px" width="18" height="8" viewBox="0 0 18 8"><path d="M0 4h16M13 1l3 3-3 3" fill="none" stroke="#c4918a"/></svg>
<div class="abs news-rule" style="top:2718px"></div>

<div class="abs news-thumb" role="img" aria-label="Coastal city waterfront under blue sky" style="top:2737px;background:linear-gradient(180deg,#4f9fe0 0%,#9fd0ee 40%,#e7e0cf 65%,#2f8aa3 100%)"></div>
<div class="abs news-date" style="left:885px;top:2739px"><svg width="16" height="14" viewBox="0 0 16 14"><rect x=".5" y="1.5" width="15" height="12" fill="none" stroke="#c4918a"/><path d="M.5 4.5h15M4 0v3M12 0v3" stroke="#c4918a"/></svg>February 28, 2024</div>
<p class="abs news-small" style="top:2762px">“New Data Finds Medtech Industry Thrives in the Sunshine State.”</p>
<svg class="abs" style="left:886px;top:2826px" width="18" height="8" viewBox="0 0 18 8"><path d="M0 4h16M13 1l3 3-3 3" fill="none" stroke="#c4918a"/></svg>
<div class="abs news-rule" style="top:2845px"></div>
<div class="abs btn-dark" style="left:744px;top:2868px;width:122px;height:34px">VIEW ALL NEWS</div>

<!-- Contact -->
<div class="abs map" role="img" aria-label="Street map of the office neighbourhood"></div>
<svg class="abs" style="left:302px;top:3170px" width="18" height="24" viewBox="0 0 18 24"><path d="M9 23C3 15 1 12 1 8a8 8 0 0 1 16 0c0 4-2 7-8 15z" fill="#e0322d"/><circle cx="9" cy="8" r="3" fill="#fff"/></svg>
<div class="abs map-card">418 Larkspur Ave, Suite<br>210, Fairhaven, MD 20714</div>

<section class="abs contact-panel"></section>
<h2 class="abs serif contact-title">For any Inquiries,<br>Please Call or Email us.</h2>
<p class="abs contact-sub">Alternatively you can fill in the following contact form.</p>
<div class="abs field" style="top:3142px;height:36px">Name</div>
<div class="abs field" style="top:3192px;height:36px">Email</div>
<div class="abs field" style="top:3240px;height:76px">Message</div>
<div class="abs btn-dark" style="left:723px;top:3330px;width:97px;height:35px">SUBMIT</div>

<!-- Footer -->
<footer class="abs footer"></footer>
<div class="abs brand" style="left:120px;top:3530px">
  <div class="brand-box" style="width:54px;height:54px"></div>
  <div><div class="brand-name" style="font-size:28px">HOLLINBROOK</div><div class="brand-sub" style="font-size:13px">COUNSEL</div></div>
</div>
<div class="abs footer-rule" style="left:389px"></div>
<div class="abs footer-rule" style="left:638px"></div>
<div class="abs footer-rule" style="left:920px"></div>

<h3 class="abs footer-head" style="left:477px">About Us</h3>
<ul class="abs footer-links">
  <li>Home</li><li>Home</li><li>Services</li><li>Research</li><li>The Institute</li><li>In the News</li><li>Contact Us</li>
</ul>

<h3 class="abs footer-head" style="left:705px">Contact Us</h3>
<div class="abs footer-item" style="left:705px;top:3486px">
  <span class="icon-ring"><svg width="15" height="15" viewBox="0 0 15 15"><path d="M7.5 12C5 9 4.5 8 4.5 6.5a3 3 0 0 1 6 0c0 1.5-.5 2.5-3 5.5z" fill="#fff"/></svg></span>
  <span>418 Larkspur Ave Suite 210<br>Fairhaven, MD 20714</span>
</div>
<div class="abs footer-item" style="left:705px;top:3530px;align-items:center">
  <span class="icon-ring"><svg width="15" height="15" viewBox="0 0 15 15"><rect x="4" y="5" width="7" height="5" fill="none" stroke="#fff" stroke-width=".9"/><path d="M4 5l3.5 3L11 5" fill="none" stroke="#fff" stroke-width=".9"/></svg></span>
  <span>info@hollinbrookcounsel.com</span>
</div>
<div class="abs footer-item" style="left:705px;top:3568px;align-items:center">
  <span class="icon-ring"><svg width="15" height="15" viewBox="0 0 15 15"><path d="M5 4l1.5 2-1 1c.5 1 1.5 2 2.5 2.5l1-1 2 1.5-1 1.5C7 11 4 8 3.5 5z" fill="#fff"/></svg></span>
  <span>+ (555) 014-2290</span>
</div>

<h3 class="abs footer-head" style="left:998px">Follow Us</h3>
<div class="abs footer-item" style="left:998px;top:3486px;align-items:center"><span class="icon-ring"></span><span>Chatterly</span></div>
<div class="abs footer-item" style="left:998px;top:3526px;align-items:center"><span class="icon-ring"></span><span>Linkwise</span></div>
<div class="abs footer-item" style="left:998px;top:3566px;align-items:center"><span class="icon-ring"></span><span>Postbird</span></div>

<div class="abs copyright-rule"></div>
<p class="abs copyright">© 2024 HOLLINBROOK COUNSEL ALL RIGHTS RESERVED</p>

</body>
</html>
```